They say laughter is the best medicine

This poster is for a nursing pharmacology class room with 70+students. Size is 24" x36". It needs to be a clean design. Would like vintage advertisement banners and script fonts. Would like a black background with an accent color. Please view pictures on word doc for examples.

```html
<!DOCTYPE html>
<html lang="en">
<head>
<meta charset="utf-8">
<title>Laughter Is the Best Medicine</title>
<link rel="stylesheet" href="https://fonts.googleapis.com/css2?family=Playball&family=Lobster&family=Oswald:wght@400;500&family=Rye&display=swap">
<style>
  :root {
    --board: #252525;
    --board-light: #333333;
    --chalk: #ffffff;
    --accent: #f7941d;
    --accent-deep: #c9701a;
    --ink: #2a2a2a;
  }
  html, body { margin: 0; padding: 0; overflow: hidden; }
  body { width: 800px; height: 1200px; background: var(--board); }
  .poster {
    position: relative;
    width: 800px; height: 1200px; overflow: hidden;
    background: radial-gradient(ellipse at 50% 40%, var(--board-light) 0%, var(--board) 70%, #1c1c1c 100%);
    color: var(--chalk);
    font-family: "Oswald", sans-serif;
  }
  .headline-art { position: absolute; left: 0; top: 0; width: 800px; height: 560px; }
  .they-say {
    position: absolute; left: 68px; top: 22px; margin: 0;
    font-family: "Playball", cursive; font-size: 66px; font-weight: 400;
    line-height: 1; color: var(--chalk);
  }
  .drug-list {
    position: absolute; left: 72px; top: 564px; width: 700px;
    display: grid; grid-template-columns: 318px 382px;
    list-style: none; margin: 0; padding: 0;
  }
  .drug-list li {
    position: relative; padding-left: 36px;
    font-family: "Oswald", sans-serif; font-weight: 400;
    font-size: 58px; line-height: 60px; letter-spacing: 1px;
    white-space: nowrap;
  }
  .drug-list li::before {
    content: ""; position: absolute; left: 2px; top: 24px;
    width: 13px; height: 13px; border-radius: 50%; background: var(--accent);
  }
  .ampersand {
    position: absolute; left: 0; width: 800px; top: 862px; margin: 0; text-align: center;
    font-family: "Playball", cursive; font-size: 50px; line-height: 1;
  }
  .final-drug {
    position: absolute; left: 0; width: 800px; top: 916px; margin: 0; text-align: center;
    font-family: "Oswald", sans-serif; font-size: 60px; line-height: 1; letter-spacing: 1px;
  }
  .illustration {
    position: absolute; border-radius: 18px; opacity: .8;
    background: linear-gradient(135deg, var(--accent), var(--accent-deep));
  }
  .illustration.pills { left: 54px; top: 876px; width: 150px; height: 94px; }
  .illustration.vials { left: 612px; top: 866px; width: 128px; height: 60px; }
  .tagline {
    position: absolute; left: 0; width: 800px; top: 988px; margin: 0; text-align: center;
    font-family: "Lobster", cursive; font-size: 33px; line-height: 1; color: var(--accent);
  }
  .credits {
    position: absolute; left: 0; width: 800px; top: 1036px; margin: 0; text-align: center;
    font-family: "Oswald", sans-serif; font-weight: 400; font-size: 27px; line-height: 30px;
    letter-spacing: .3px; text-transform: uppercase;
  }
  .credits p { margin: 0; }
  .flourish { position: absolute; background: var(--accent); opacity: .6; border-radius: 30px; }
  .flourish.left { left: 64px; top: 1048px; width: 60px; height: 62px; }
  .flourish.right { left: 676px; top: 1048px; width: 60px; height: 62px; }
  .flourish.bottom { left: 250px; top: 1134px; width: 300px; height: 30px; }
</style>
</head>
<body>
<main class="poster">
  <p class="they-say">They Say,</p>

  <svg class="headline-art" viewBox="0 0 800 560" aria-label="Laughter is the best medicine! Well, we think">
    <text x="60" y="160" fill="var(--accent)" font-family="Lobster, cursive" font-size="110">“</text>
    <text x="588" y="290" fill="var(--accent)" font-family="Lobster, cursive" font-size="100">”</text>

    <text x="118" y="180" fill="var(--chalk)" font-family="Oswald, sans-serif" font-size="84" letter-spacing="2">LAUGHTER IS THE</text>

    <path d="M64,205 Q105,190 130,222 C190,520 610,520 728,75 L765,42" fill="none" stroke="var(--accent)" stroke-width="6" stroke-linecap="round"/>
    <path d="M98,198 Q120,188 148,196" fill="none" stroke="var(--chalk)" stroke-width="2"/>
    <path d="M106,244 C140,320 170,360 205,382" fill="none" stroke="var(--chalk)" stroke-width="2"/>
    <path d="M740,155 C722,280 665,360 590,398" fill="none" stroke="var(--chalk)" stroke-width="2"/>

    <text x="400" y="272" text-anchor="middle" fill="var(--chalk)" font-family="Lobster, cursive" font-size="80">best</text>
    <path d="M272,228 l30,10 l-30,12 z M528,228 l-30,10 l30,12 z" fill="var(--accent)"/>

    <path id="medicineArc" d="M155,240 Q400,550 650,230" fill="none"/>
    <text fill="var(--chalk)" font-family="Rye, serif" font-size="76">
      <textPath href="#medicineArc" startOffset="50%" text-anchor="middle">MEDICINE!</textPath>
    </text>

    <path d="M110,398 Q130,430 160,445" fill="none" stroke="var(--chalk)" stroke-width="9" stroke-linecap="round"/>
    <path d="M700,395 Q670,415 640,438" fill="none" stroke="var(--chalk)" stroke-width="9" stroke-linecap="round"/>
    <path d="M130,432 L182,408 L200,492 L148,472 L176,456 Z" fill="var(--chalk)"/>
    <path d="M612,436 L728,482 L662,492 L640,486 Z" fill="var(--chalk)"/>
    <path d="M178,400 Q400,570 620,430 L640,484 Q410,600 196,500 Z" fill="var(--chalk)"/>
    <path id="bannerArc" d="M196,468 Q400,600 628,462" fill="none"/>
    <text fill="var(--ink)" font-family="Rye, serif" font-size="42">
      <textPath href="#bannerArc" startOffset="50%" text-anchor="middle">WELL, WE THINK</textPath>
    </text>
    <circle cx="365" cy="453" r="5" fill="var(--accent)"/>
    <circle cx="520" cy="432" r="5" fill="var(--accent)"/>
    <circle cx="272" cy="540" r="5" fill="var(--accent)"/>
    <circle cx="532" cy="537" r="5" fill="var(--accent)"/>
    <circle cx="642" cy="505" r="5" fill="var(--accent)"/>
  </svg>

  <ul class="drug-list">
    <li>FEVRINOL</li><li>HALTROL</li>
    <li>CALMIVAN</li><li>STOPIUM AD</li>
    <li>MSO4</li><li>ALBUTEROL</li>
    <li>FLUSHIX</li><li>VANCOMYCIN</li>
    <li>OXYGEN</li><li>INSULIN</li>
  </ul>

  <div class="illustration pills" role="img" aria-label="Engraved illustration of an open pill bottle with spilled capsules"></div>
  <div class="illustration vials" role="img" aria-label="Engraved illustration of a syringe and medicine vials"></div>

  <p class="ampersand">&amp;</p>
  <p class="final-drug">NITROGLYCERIN</p>

  <p class="tagline">Just might be what you want more in certain situations.</p>

  <div class="flourish left" role="img" aria-label="Decorative orange scroll flourish"></div>
  <div class="flourish right" role="img" aria-label="Decorative orange scroll flourish"></div>
  <div class="flourish bottom" role="img" aria-label="Decorative orange scroll flourish"></div>

  <div class="credits">
    <p>Nursing Pharmacology Concepts</p>
    <p>Delia Harwood, PhD, MSN, RN, CCRN, CPN, CNE</p>
    <p>Clinical Professor</p>
  </div>
</main>
</body>
</html>
```